Quem fala que não existe perfeição, com certeza não conheceu os serviços da Casa Traço Vivo! 100% satisfeita com os serviços oferecidos, desde a vendedora Marília ao gestor Caio, muito atenciosos e prestativos!!!

```html
<!DOCTYPE html>
<html lang="pt-BR">
<head>
<meta charset="utf-8">
<title>Casa Traço Vivo — Papel timbrado</title>
<link href="https://fonts.googleapis.com/css2?family=Montserrat:wght@400;600;800&display=swap" rel="stylesheet">
<style>
  :root {
    --backdrop: #e9e9e7;
    --paper: #ffffff;
    --ink: #1b1b1b;
    --muted: #444444;
    --gold: #c9a53a;
    --gold-light: #e8cd73;
    --gold-dark: #a9821f;
    --watermark: #ececec;
  }
  * { box-sizing: border-box; margin: 0; padding: 0; }
  html, body {
    width: 1200px; height: 1200px; overflow: hidden;
    background: var(--backdrop);
    font-family: "Montserrat", sans-serif;
    color: var(--ink);
  }
  .letterhead {
    position: absolute; left: 240px; top: 48px;
    width: 720px; height: 1080px;
    background: var(--paper);
    box-shadow: 0 2px 10px rgba(0,0,0,0.12);
  }
  .brand {
    position: absolute; top: 22px; left: 0; width: 100%;
    display: flex; flex-direction: column; align-items: center;
  }
  .brand-dot {
    width: 40px; height: 40px; border-radius: 50%;
    background: var(--gold);
    margin-bottom: 8px;
  }
  .brand-name {
    font-weight: 800; font-size: 22px; letter-spacing: 0.5px;
    line-height: 1; color: var(--ink); text-transform: uppercase;
  }
  .brand-tagline {
    margin-top: 5px;
    font-weight: 600; font-size: 8px; letter-spacing: 4px;
    text-transform: uppercase; color: var(--ink);
  }
  .watermark {
    position: absolute; left: 144px; top: 348px;
    width: 432px; height: 432px;
    border: 46px solid var(--watermark);
    border-radius: 50%;
    display: flex; align-items: center; justify-content: center;
  }
  .watermark-name {
    font-weight: 800; font-size: 30px; letter-spacing: 1px;
    color: var(--watermark); text-transform: uppercase; white-space: nowrap;
  }
  .contacts {
    position: absolute; left: 14px; top: 934px;
    list-style: none;
    font-size: 8px; line-height: 14px; color: var(--muted);
  }
  .contacts li { display: flex; align-items: center; gap: 5px; }
  .contacts svg { width: 8px; height: 8px; flex: none; }
  .footer-bar {
    position: absolute; left: 8px; top: 1026px;
    width: 646px; height: 7px;
    background: linear-gradient(90deg, var(--gold-dark), var(--gold-light) 45%, var(--gold) 75%, var(--gold-light));
    clip-path: polygon(0 0, 100% 0, 98.5% 100%, 0 100%);
  }
</style>
</head>
<body>
  <main class="letterhead">
    <header class="brand">
      <span class="brand-dot"></span>
      <span class="brand-name">Casa Traço Vivo</span>
      <span class="brand-tagline">Controle de pragas</span>
    </header>

    <div class="watermark" aria-hidden="true">
      <span class="watermark-name">Casa Traço Vivo</span>
    </div>

    <ul class="contacts">
      <li>CNPJ: 00.000.000/0001-00</li>
      <li>
        <svg viewBox="0 0 10 10"><circle cx="5" cy="5" r="5" fill="var(--gold)"/><path d="M3.2 2.6l1 .9-.5.8c.4.8 1 1.4 1.8 1.8l.8-.5.9 1-.7.8C4.6 7.2 2.8 5.4 2.6 3.3z" fill="#fff"/></svg>
        12 3400-1188
      </li>
      <li>
        <svg viewBox="0 0 10 10"><circle cx="5" cy="5" r="5" fill="var(--gold)"/><rect x="2.5" y="3.3" width="5" height="3.4" fill="none" stroke="#fff" stroke-width=".7"/><path d="M2.5 3.3L5 5.2l2.5-1.9" fill="none" stroke="#fff" stroke-width=".7"/></svg>
        contato@casatracovivo.com
      </li>
      <li>
        <svg viewBox="0 0 10 10"><circle cx="5" cy="5" r="5" fill="var(--gold)"/><circle cx="5" cy="5" r="2.4" fill="none" stroke="#fff" stroke-width=".7"/><path d="M2.6 5h4.8M5 2.6v4.8" stroke="#fff" stroke-width=".6"/></svg>
        www.casatracovivo.com
      </li>
      <li>
        <svg viewBox="0 0 10 10"><circle cx="5" cy="5" r="5" fill="var(--gold)"/><circle cx="5" cy="5" r="1.3" fill="none" stroke="#fff" stroke-width=".7"/></svg>
        @casatracovivo
      </li>
    </ul>

    <div class="footer-bar"></div>
  </main>
</body>
</html>
```